Robotic Physical Therapy office needs a Grand Opening Flyer

We need a Grand Opening flyer design for a robotic physical therapy office named Stellar Motion Therapy. We would like it to have a clean, classy, upscale feeling that gives potential clients a V.I.P. feeling. We would like to use the colors black, gray, and yellow (logo will be uploaded).

Event: Thursday, June 1st, 2023 from 12pm-6pm
location: 58274 Harlow Ave, Bloomfield Hills, MI 48319

Industry/Entity Type

Physical therapy

Font styles to use
Script

Colors

Designer to choose colors to be used in the design.

Requirements
Nice to have
• More of a vip feel for the invite

```html
<!DOCTYPE html>
<html lang="en">
<head>
<meta charset="UTF-8">
<title>Stellar Motion Therapy – Grand Opening</title>
<link rel="stylesheet" href="https://fonts.googleapis.com/css2?family=Anton&family=Poppins:wght@300;400;600;700&family=Yellowtail&display=swap">
<style>
  :root {
    --page-bg: #d9d9d9;
    --flyer-bg: #151515;
    --flyer-glow: #2e2c26;
    --yellow: #f5c814;
    --white: #ffffff;
    --ink: #111111;
    --photo-light: #bfc3c7;
    --photo-mid: #6e6a66;
    --photo-skin: #8a5a3c;
  }
  * { margin: 0; padding: 0; box-sizing: border-box; }
  html, body {
    width: 682px; height: 1200px; overflow: hidden;
    background: var(--page-bg);
    font-family: "Poppins", sans-serif;
  }
  .canvas { position: relative; width: 682px; height: 1200px; }
  .flyer {
    position: absolute; left: 31px; top: 203px;
    width: 620px; height: 794px; overflow: hidden;
    background: radial-gradient(ellipse at 50% 55%, var(--flyer-glow) 0%, var(--flyer-bg) 65%);
    box-shadow: 0 10px 30px rgba(0,0,0,.25);
  }
  .brand {
    position: absolute; top: 40px; left: 0; width: 100%;
    display: flex; justify-content: center; align-items: center; gap: 12px;
  }
  .brand-mark {
    width: 34px; height: 34px; border-radius: 50%;
    background: var(--white);
  }
  .brand-name {
    color: var(--white); font-weight: 600; font-size: 24px;
    letter-spacing: .5px; line-height: 1; text-transform: uppercase;
  }
  .invite-line {
    position: absolute; top: 135px; width: 100%; text-align: center;
    color: var(--white); font-weight: 300; font-size: 21px; letter-spacing: 1.5px;
    line-height: 1.2;
  }
  .title-grand {
    position: absolute; top: 172px; width: 100%; text-align: center;
    font-family: "Anton", "Impact", sans-serif; color: var(--white);
    font-size: 112px; line-height: 1; letter-spacing: 2px; font-weight: 400;
  }
  .title-opening {
    position: absolute; top: 280px; width: 100%; text-align: center;
    font-family: "Yellowtail", "Brush Script MT", cursive; color: var(--yellow);
    font-size: 88px; line-height: 1; transform: rotate(-5deg);
    padding-left: 40px;
  }
  .hero-photo {
    position: absolute; top: 395px; left: 130px; width: 360px; height: 175px;
    border-radius: 12px;
    background: linear-gradient(100deg, var(--photo-light) 0%, var(--photo-mid) 50%, var(--photo-skin) 100%);
    opacity: .9;
  }
  .event-info {
    position: absolute; top: 592px; left: 48px; width: 524px; height: 112px;
    display: flex;
  }
  .event-date, .event-place {
    flex: 1; display: flex; align-items: center; gap: 14px; padding: 0 18px;
    font-size: 18px; line-height: 1.35;
  }
  .event-date { background: var(--yellow); color: var(--ink); font-weight: 600; }
  .event-place {
    background: var(--flyer-bg); color: var(--white);
    border: 2px solid var(--yellow); font-weight: 400;
  }
  .event-place .icon { color: var(--yellow); }
  .icon { flex: none; width: 28px; height: 28px; }
  sup { font-size: .6em; line-height: 0; }
</style>
</head>
<body>
<div class="canvas">
  <article class="flyer">
    <header class="brand">
      <span class="brand-mark"></span>
      <span class="brand-name">Stellar Motion Therapy</span>
    </header>

    <p class="invite-line">You are invited to our</p>
    <h1 class="title-grand">GRAND</h1>
    <p class="title-opening">Opening</p>

    <div class="hero-photo" role="img" aria-label="Robotic hand and human hand bumping fists"></div>

    <section class="event-info">
      <div class="event-date">
        <svg class="icon" viewBox="0 0 24 24" fill="none" stroke="currentColor" stroke-width="2">
          <rect x="3" y="5" width="18" height="16" rx="2"/>
          <line x1="3" y1="10" x2="21" y2="10"/>
          <line x1="8" y1="2" x2="8" y2="7"/>
          <line x1="16" y1="2" x2="16" y2="7"/>
        </svg>
        <p>Thursday,<br>June 1<sup>st</sup>, 2023<br>12pm to 6pm</p>
      </div>
      <div class="event-place">
        <svg class="icon" viewBox="0 0 24 24" fill="none" stroke="currentColor" stroke-width="2">
          <path d="M12 22s7-7.2 7-12.5A7 7 0 0 0 5 9.5C5 14.8 12 22 12 22z"/>
          <circle cx="12" cy="9.5" r="2.5"/>
        </svg>
        <p>58274 Harlow Ave,<br>Larkspur Hills,<br>WA 48319</p>
      </div>
    </section>
  </article>
</div>
</body>
</html>
```